Book Cover Design Project

Cover design using photo provided.
Title is as follows:-

Harold Edmund Pellow

"Letters from the Quiet Orchard"

By Dennis Halloway

Just Added Picture and extended design a further 7 days

```html
<!DOCTYPE html>
<html lang="en">
<head>
<meta charset="utf-8">
<title>Harold Edmund Pellow — Letters from the Quiet Orchard</title>
<link rel="stylesheet" href="https://fonts.googleapis.com/css2?family=Cinzel:wght@700&family=Crimson+Text:wght@400&family=Oswald:wght@700&family=Roboto:wght@700&display=swap">
<style>
  :root {
    --ink-red: #8e1a1c;
    --ink-red-deep: #5e0f11;
    --paper-white: #f4f4f2;
    --map-dark: #2a2c2e;
    --map-mid: #55585b;
    --map-light: #8a8d90;
    --portrait-warm: #b49a78;
    --portrait-dark: #2d2a2a;
  }
  * { margin: 0; padding: 0; box-sizing: border-box; }
  html, body { width: 793px; height: 1200px; overflow: hidden; background: var(--map-dark); }
  .cover {
    position: relative;
    width: 793px;
    height: 1200px;
    overflow: hidden;
  }
  .cover__backdrop {
    position: absolute;
    inset: 0;
    background:
      radial-gradient(ellipse at 70% 25%, rgba(180,182,185,0.35), transparent 55%),
      radial-gradient(ellipse at 20% 70%, rgba(140,142,145,0.3), transparent 50%),
      radial-gradient(ellipse at 85% 85%, rgba(200,202,205,0.3), transparent 45%),
      linear-gradient(160deg, var(--map-mid) 0%, var(--map-dark) 45%, var(--map-mid) 75%, var(--map-light) 100%);
  }
  .cover__subject {
    position: absolute;
    top: 22px;
    left: 0;
    width: 100%;
    text-align: center;
    font-family: "Cinzel", serif;
    font-weight: 700;
    font-size: 46px;
    letter-spacing: 1px;
    color: var(--ink-red);
    text-shadow: 0 1px 2px rgba(0,0,0,0.5);
  }
  .cover__rule {
    position: absolute;
    top: 86px;
    left: 48px;
    width: 697px;
    height: 3px;
    background: var(--paper-white);
  }
  .cover__kicker {
    position: absolute;
    top: 104px;
    left: 0;
    width: 100%;
    text-align: center;
    font-family: "Crimson Text", serif;
    font-size: 44px;
    color: var(--paper-white);
    text-shadow: 0 2px 4px rgba(0,0,0,0.6);
  }
  .cover__portrait {
    position: absolute;
    top: 172px;
    left: 206px;
    width: 418px;
    height: 520px;
    background: var(--paper-white);
    padding: 14px;
    box-shadow: 0 4px 14px rgba(0,0,0,0.6);
  }
  .cover__portrait-photo {
    width: 100%;
    height: 100%;
    background: linear-gradient(180deg, var(--portrait-warm) 0%, #a08563 50%, var(--portrait-dark) 78%, #1e1c1d 100%);
  }
  .cover__title {
    position: absolute;
    top: 740px;
    left: 40px;
    width: 713px;
    height: 290px;
  }
  .cover__title text {
    font-family: "Oswald", sans-serif;
    font-weight: 700;
    fill: var(--ink-red);
    stroke: var(--ink-red-deep);
    stroke-width: 1;
  }
  .cover__author {
    position: absolute;
    top: 1030px;
    left: 0;
    width: 100%;
    text-align: center;
    font-family: "Roboto", sans-serif;
    font-weight: 700;
    font-size: 60px;
    color: var(--paper-white);
    text-shadow: 0 2px 4px rgba(0,0,0,0.7);
  }
</style>
</head>
<body>
  <main class="cover">
    <div class="cover__backdrop" role="img" aria-label="Aerial black-and-white photograph of a city seen from above"></div>
    <h2 class="cover__subject">Harold Edmund Pellow</h2>
    <div class="cover__rule"></div>
    <p class="cover__kicker">Letters from the</p>
    <figure class="cover__portrait">
      <div class="cover__portrait-photo" role="img" aria-label="Hand-tinted portrait photograph of a man in a service uniform and cap"></div>
    </figure>
    <svg class="cover__title" viewBox="0 0 713 290" aria-label="Quiet Orchard">
      <text x="356" y="135" text-anchor="middle" font-size="130" textLength="690" lengthAdjust="spacingAndGlyphs" transform="scale(1,1)">QUIET</text>
      <text x="356" y="280" text-anchor="middle" font-size="140" textLength="700" lengthAdjust="spacingAndGlyphs">ORCHARD</text>
    </svg>
    <p class="cover__author">By Dennis Halloway</p>
  </main>
</body>
</html>
```